Government Contracting business needs a website design.

Brisco & Wendell, LLC is a minority owned Service Disabled Veteran Owned Small Business (SDVOSB) that provides Strategic Planning, Public Health Emergency Response, and Data Management Solutions for Federal Civilian and Defense Agencies. We have over 20 years of experience helping health and defense agencies develop concept of operations, deploy assets and personnel in Hot Zones around the world, and deliver goods and services all of the globe.

We are a leader in the field of Data Management. We help our customers develop cloud migration and disaster recovery strategies. We are experts with database management, data replication, queries, consolidation, and records management.

We are looking for a very nice and simple website designs that states clearly what we do as a company and that is easy for our customers to follow. We would like to have some moving pictures that are base on our expertise. We want the website to be easy to use and have the scroll down features that keeps things all on the same page when clicking on the menu. I attached a document with what we need on the website. I will also attach our logo. We want it to look simple clean and very professional.

Target Market(s)

Government Contracting, Management Consulting, Health

Industry/Entity Type

Government

Coding

Coded - Design and coding required

Number of Pages Required

1 page

Font styles to use
Serif

Requirements
Must have
• Very nice picture slides that speaks to our capabilities in Disaster Response, Strategic Planning, and Database Management. Slick look and design. Make sure SDVOSB Logo is right at the beginning of website as our customers is looking for that certification. Very nice colors that blend well with our logo.
Nice to have
• Very nice and slick colors that blends well with logo.
Should not have
• Basic website design that are weary on the eye. No bright colors, just simple colors that looks good with logo.

```html
<!DOCTYPE html>
<html lang="en">
<head>
<meta charset="utf-8">
<title>Brisco &amp; Wendell, LLC – SDVOSB Financial Advocate</title>
<link rel="stylesheet" href="https://fonts.googleapis.com/css2?family=Poppins:wght@300;400;500;600&family=Roboto+Condensed:wght@300;400&display=swap">
<style>
:root{
  --navy:#0b3d7e;
  --blue:#1556a8;
  --red:#c4121b;
  --ink:#222222;
  --muted:#6b6b6b;
  --grey-box:#e6e6e6;
  --grey-panel:#dedede;
  --footer:#1e1e1e;
  --footer-line:#333333;
  --footer-text:#b8b8b8;
  --white:#ffffff;
}
*{box-sizing:border-box;margin:0;padding:0}
html,body{width:1200px;height:3797px;overflow:hidden}
body{font-family:"Poppins",sans-serif;color:var(--ink);background:var(--white);position:relative}

/* header */
.site-header{position:absolute;top:0;left:0;width:1200px;height:114px;background:var(--white);z-index:2}
.brand{position:absolute;left:88px;top:22px;display:flex;align-items:center;gap:12px}
.brand-mark{width:62px;height:62px;border-radius:50%;background:var(--navy)}
.brand-name{font-size:17px;font-weight:600;color:var(--navy)}
.social{position:absolute;top:22px;left:742px;display:flex;gap:17px}
.social span{width:23px;height:23px;border-radius:50%;background:var(--red);display:block}
.login-btn{position:absolute;left:970px;top:14px;width:144px;height:40px;background:var(--blue);color:var(--white);font-size:14px;display:flex;align-items:center;justify-content:center}
.main-nav{position:absolute;top:70px;left:0;width:1200px;font-size:13px;font-weight:500;color:var(--ink)}
.main-nav a{position:absolute;white-space:nowrap;text-decoration:none;color:inherit;transform:translateX(-50%)}
.main-nav i{position:absolute;top:2px;width:1px;height:14px;background:#999}

/* hero */
.hero{position:absolute;top:114px;left:0;width:1200px;height:585px;background:linear-gradient(100deg,#3b2418 0%,#7a4a2a 30%,#e3a15a 48%,#f5d8a0 55%,#9a6a45 75%,#5a3a28 100%)}
.hero-card{position:absolute;left:144px;top:58px;width:413px;height:461px;background:rgba(40,90,170,.78);color:var(--white);text-align:center}
.hero-frame{position:absolute;left:24px;top:30px;right:24px;bottom:30px;border:1px solid rgba(255,255,255,.7)}
.hero-welcome{font-family:"Roboto Condensed",sans-serif;font-weight:300;font-size:38px;margin-top:70px}
.hero-title{font-family:"Roboto Condensed",sans-serif;font-size:48px;letter-spacing:2px;margin-top:28px}
.hero-sub{font-family:"Roboto Condensed",sans-serif;font-size:30px;margin-top:4px}
.hero-rule{width:260px;height:1px;background:rgba(255,255,255,.6);margin:30px auto 0}
.hero-btn{display:inline-block;margin-top:40px;background:var(--red);color:var(--white);font-size:16px;padding:18px 32px;border-radius:30px}

/* shared */
.section-title{position:absolute;left:0;width:1200px;text-align:center;font-size:44px;font-weight:500;letter-spacing:1px}
.section-lead{position:absolute;left:140px;width:920px;text-align:center;font-size:14px;line-height:30px;color:var(--muted)}
.pill{display:inline-flex;align-items:center;justify-content:center;background:var(--red);color:var(--white);border-radius:30px}

/* services */
.service{position:absolute;top:953px;width:238px;height:146px}
.service-icon{position:absolute;left:50%;top:0;transform:translateX(-50%);width:92px;height:92px;border-radius:50%;background:var(--white);border:2px solid #d0d0d0;z-index:1;display:flex;align-items:center;justify-content:center}
.service-label{position:absolute;left:0;top:77px;width:100%;height:69px;background:var(--grey-box);display:flex;align-items:center;justify-content:center;padding-top:14px;font-size:18px;color:#333;white-space:nowrap}

/* about */
.about-photo{position:absolute;left:0;top:1190px;width:587px;height:387px;background:linear-gradient(135deg,#8fae5a,#c9a27e 50%,#e6d3bf)}
.about-panel{position:absolute;left:608px;top:1190px;width:592px;height:387px;background:var(--grey-panel);padding:44px 44px 0 44px}
.about-panel h2{font-size:32px;font-weight:500;letter-spacing:3px}
.about-rule{width:50px;height:2px;background:#999;margin:22px 0 28px}
.about-panel p{font-size:13px;line-height:27px;color:#555}
.about-btn{display:inline-flex;margin-top:30px;width:134px;height:46px;border-radius:24px;background:#8e8e8e;color:var(--white);font-size:13px;align-items:center;justify-content:center}

/* why hire */
.reason{position:absolute;top:1863px;width:238px;height:360px;border:1px solid #d8d8d8;text-align:center}
.reason-photo{height:208px;margin:-1px -1px 0}
.reason p{font-size:11px;line-height:24px;color:#555;padding:16px 12px 0}
.reason .pill{position:absolute;left:50%;bottom:-22px;transform:translateX(-50%);width:134px;height:44px;font-size:13px}

/* testimonial */
.quote-band{position:absolute;left:0;top:2400px;width:1200px;height:124px;background:var(--navy)}
.quote-avatar{position:absolute;left:91px;top:2370px;width:157px;height:157px;border-radius:50%;background:linear-gradient(160deg,#e9c98a,#c99a6a);border:5px solid var(--white);z-index:1}
.quote-text{position:absolute;left:298px;top:2432px;font-size:21px;color:var(--white)}
.quote-name{position:absolute;left:298px;top:2475px;font-size:12px;color:#a9c2e6;letter-spacing:1px}

/* team */
.member{position:absolute;top:2572px;width:499px;text-align:center}
.member-photo{height:304px}
.member h3{font-size:27px;font-weight:400;margin-top:48px}
.member .role{font-size:16px;color:#8a8a8a;letter-spacing:1px;margin-top:4px}
.member p{font-size:14px;line-height:28px;color:#555;margin:30px 24px 0;height:118px}
.member .pill{width:184px;height:58px;font-size:20px;margin-top:16px}

/* footer */
.site-footer{position:absolute;left:0;top:3337px;width:1200px;height:460px;background:var(--footer);color:var(--footer-text)}
.footer-brand{position:absolute;left:160px;top:22px;display:flex;flex-direction:column;align-items:center;gap:8px}
.footer-brand .brand-mark{width:90px;height:90px;background:#163a73}
.footer-brand .brand-name{color:#3c5f99;font-size:14px}
.contact-line{position:absolute;left:86px;width:280px;font-size:14px;line-height:24px;display:flex;gap:16px;align-items:flex-start;padding-bottom:14px;border-bottom:1px solid var(--footer-line)}
.contact-line svg{flex:none;margin-top:4px}
.footer-col-title{position:absolute;font-size:15px;color:#e6e6e6}
.footer-links{position:absolute;left:519px;top:139px;list-style:none;font-size:12px;letter-spacing:1px}
.footer-links li{height:44px;display:flex;align-items:center;gap:16px}
.footer-links li::before{content:"";width:12px;height:12px;border:1px solid #888;border-radius:50%}
.newsletter-note{position:absolute;left:825px;top:131px;width:300px;font-size:13px;line-height:25px}
.newsletter-input{position:absolute;left:825px;top:218px;width:286px;height:43px;border:1px solid #777;font-size:12px;color:#999;padding:13px 20px}
.subscribe-btn{position:absolute;left:825px;top:286px;width:130px;height:44px;background:var(--red);color:var(--white);font-size:15px;display:flex;align-items:center;justify-content:center}
.footer-bottom{position:absolute;left:0;top:405px;width:1200px;border-top:1px solid var(--footer-line);text-align:center;font-size:12px;color:#888;padding-top:20px}
</style>
</head>
<body>

<header class="site-header">
  <div class="brand"><span class="brand-mark"></span><span class="brand-name">Brisco &amp; Wendell</span></div>
  <div class="social"><span></span><span></span><span></span><span></span><span></span></div>
  <div class="login-btn">Visitor's login</div>
  <nav class="main-nav">
    <a style="left:360px">About Us</a>
    <i style="left:433px"></i>
    <a style="left:496px">Team</a>
    <i style="left:566px"></i>
    <a style="left:663px">Core Capabilities</a>
    <i style="left:772px"></i>
    <a style="left:881px">Agencies We Serve</a>
    <i style="left:992px"></i>
    <a style="left:1074px">Contact us</a>
  </nav>
</header>

<section class="hero" role="img" aria-label="Woman on a balcony at sunset with warm backlight over hills">
  <div class="hero-card">
    <div class="hero-frame"></div>
    <div class="hero-welcome">Welcome To</div>
    <div class="hero-title">SDVOSB</div>
    <div class="hero-sub">Financial advocate</div>
    <div class="hero-rule"></div>
    <div class="hero-btn">Schedule an Appointment</div>
  </div>
</section>

<h2 class="section-title" style="top:765px">Our Services</h2>
<p class="section-lead" style="top:842px">Lorem ipsum dolor sit amet, consectetur adipiscing elit, sed do eiusmod tempor incididunt ut labore et dolore magna aliqua. Ut enim ad minim veniam,</p>

<div class="service" style="left:86px">
  <div class="service-icon"><svg width="48" height="48" viewBox="0 0 48 48"><rect x="8" y="26" width="8" height="14" fill="#c4121b"/><rect x="20" y="16" width="8" height="24" fill="#c4121b"/><rect x="32" y="8" width="8" height="32" fill="#c4121b"/></svg></div>
  <div class="service-label">Strategic Planning</div>
</div>
<div class="service" style="left:349px">
  <div class="service-icon"><svg width="48" height="48" viewBox="0 0 48 48"><path d="M24 26l-9-9a5 5 0 017-7l2 2 2-2a5 5 0 017 7z" fill="#c4121b"/><path d="M6 34h12l8 3 14-7v5l-14 7-8-2H6z" fill="#c4121b"/></svg></div>
  <div class="service-label">Public Health</div>
</div>
<div class="service" style="left:613px">
  <div class="service-icon"><svg width="48" height="48" viewBox="0 0 48 48"><circle cx="22" cy="28" r="12" fill="#c4121b"/><text x="22" y="33" font-family="Poppins,sans-serif" font-size="14" fill="#fff" text-anchor="middle">$</text><path d="M34 4l8 10h-5v8h-6v-8h-5z" fill="#c4121b"/></svg></div>
  <div class="service-label">Data Management</div>
</div>
<div class="service" style="left:871px">
  <div class="service-icon"><svg width="48" height="48" viewBox="0 0 48 48"><rect x="12" y="6" width="22" height="30" fill="none" stroke="#c4121b" stroke-width="3"/><path d="M17 14h12M17 20h12M17 26h8" stroke="#c4121b" stroke-width="2.5"/><path d="M24 42l6-10 8 4-6 8z" fill="#c4121b"/></svg></div>
  <div class="service-label">Contracts Vehicles</div>
</div>

<div class="about-photo" role="img" aria-label="Smiling family of three outdoors in a park"></div>
<section class="about-panel">
  <h2>ABOUT US</h2>
  <div class="about-rule"></div>
  <p>Brisco &amp; Wendell, LLC is a minority owned Service Disabled Veteran Owned Small Business (SDVOSB) that provides Strategic Planning, Public Health Emergency Response, and Data Management Solutions for Federal Civilian and Defense Agencies.</p>
  <span class="about-btn">Learn More</span>
</section>

<h2 class="section-title" style="top:1680px">Why Hire Us?</h2>
<p class="section-lead" style="top:1753px">Lorem ipsum dolor sit amet, consectetur adipiscing elit, sed do eiusmod tempor incididunt ut labore et dolore magna aliqua. Ut enim ad minim veniam,</p>

<div class="reason" style="left:86px">
  <div class="reason-photo" role="img" aria-label="Hands holding an open wallet" style="background:linear-gradient(150deg,#8a6f66,#5a2a2a)"></div>
  <p>Over 20 years of experience deploying assets and personnel to disaster zones around the US and the world.</p>
  <span class="pill">Learn More</span>
</div>
<div class="reason" style="left:349px">
  <div class="reason-photo" role="img" aria-label="Hands holding a metal cup" style="background:linear-gradient(150deg,#6a5a4e,#2e2824)"></div>
  <p>Over 20 years of experience developing concept of operations and stakeholder management strategies for Federal Agencies.</p>
  <span class="pill">Learn More</span>
</div>
<div class="reason" style="left:613px">
  <div class="reason-photo" role="img" aria-label="Hand passing a small house model and keys" style="background:linear-gradient(150deg,#a8857a,#6a4a44)"></div>
  <p>Over 10 years of experience with database management and replications.</p>
  <span class="pill">Learn More</span>
</div>
<div class="reason" style="left:871px">
  <div class="reason-photo" role="img" aria-label="Elderly man with a child indoors" style="background:linear-gradient(150deg,#9a8a7c,#4e3e36)"></div>
  <p>Highly educated consultants with over 90% possessing advance degrees and industry certifications.</p>
  <span class="pill">Learn More</span>
</div>

<div class="quote-band"></div>
<div class="quote-avatar" role="img" aria-label="Portrait of the company owner"></div>
<p class="quote-text">Lorem Ipsum is simply dummy text of the printing and typesetting industry.</p>
<p class="quote-name">MARA QUINLAN, OWNER</p>

<div class="member" style="left:86px">
  <div class="member-photo" role="img" aria-label="Portrait of the chief executive officer" style="background:linear-gradient(135deg,#d8d8d8,#9a8a80)"></div>
  <h3>Ret. SFC Dale R. Morrow</h3>
  <div class="role">Chief Executive Office</div>
  <p>Brisco &amp; Wendell, LLC was founded by Retired Sergeant First Class (Ret. SFC) Dale R. Morrow. Mr. Morrow retired from the US Army after over 20 years of service which included tours in "Operation Desert Storm/Shield".</p>
  <span class="pill">View More</span>
</div>
<div class="member" style="left:613px">
  <div class="member-photo" role="img" aria-label="Portrait of the business development manager" style="background:linear-gradient(135deg,#2a2218,#7a5a3a 50%,#1a1612)"></div>
  <h3>Mr. Nathan P. Corliss</h3>
  <div class="role">Business Development Manager</div>
  <p>Mr. Corliss brings over 10 years of business development experience to Brisco &amp; Wendell LLC. Prior to joining, Mr. Corliss led business development capture for large and midsize defense</p>
  <span class="pill">View More</span>
</div>

<footer class="site-footer">
  <div class="footer-brand"><span class="brand-mark"></span><span class="brand-name">Brisco &amp; Wendell</span></div>
  <div class="contact-line" style="top:170px"><svg width="14" height="18" viewBox="0 0 14 18"><path d="M7 1a6 6 0 016 6c0 4-6 10-6 10S1 11 1 7a6 6 0 016-6z" fill="none" stroke="#999" stroke-width="1.5"/><circle cx="7" cy="7" r="2" fill="#999"/></svg><span>12th Floor, 400 Harbor Point Drive<br>Norfolk VA 23510</span></div>
  <div class="contact-line" style="top:242px"><svg width="16" height="16" viewBox="0 0 16 16"><path d="M3 1l3 3-2 2c1 2 3 4 5 5l2-2 3 3-2 3C7 15 1 9 1 3z" fill="none" stroke="#999" stroke-width="1.5"/></svg><span>Telephone : 555 0142 7781</span></div>
  <div class="contact-line" style="top:310px;border-bottom:none"><svg width="16" height="12" viewBox="0 0 16 12"><rect x="1" y="1" width="14" height="10" fill="none" stroke="#999" stroke-width="1.5"/><path d="M1 1l7 6 7-6" fill="none" stroke="#999" stroke-width="1.5"/></svg><span>Email : info@briscowendell.com</span></div>

  <div class="footer-col-title" style="left:519px;top:85px">Our company</div>
  <ul class="footer-links">
    <li>HOME</li><li>ABOUT US</li><li>OUR PROJECTS</li><li>PROPERTY PROJECTS</li><li>CONTACT</li>
  </ul>

  <div class="footer-col-title" style="left:825px;top:88px">Sign up to newsletter</div>
  <p class="newsletter-note">You may unsubscribe at any moment. For that purpose, the legal notice.</p>
  <div class="newsletter-input">Enter Your Email ID...</div>
  <div class="subscribe-btn">Subscribe</div>

  <div class="footer-bottom">© 2017 SDVOSB - All Rights Reserved</div>
</footer>

</body>
</html>
```